Business is backhoe and truck hire. As the title indicates, we dig dirt. Colours preferred are charcoal, red and or orange. Would like a backhoe on the card,possibly a designs with the silhouette of the machine in the background. I We would like to incorporate a large tick in the title for solutions. I thought it could be part of the "W" . Our shirts are Black polo's with orange lines around sleeves and sides. We are a new business in rural Qld, happy to do the smaller jobs that others wont.

Industry/Entity Type

Business

Contact Information for Business Card

Tall Creek Groundworks Solutions

Backhoe and Truck Hire
ABN:58214096371

Peter Kellow
PH: 0491 736 204
PH: 0491 862 035
PH: 4283 6147 a/h

email: tcgsolutions@mailbox-example.com

```html
<!DOCTYPE html>
<html lang="en">
<head>
<meta charset="utf-8">
<title>Tall Creek Groundworks Solutions – Business Card</title>
<link rel="stylesheet" href="https://fonts.googleapis.com/css2?family=Alfa+Slab+One&family=Libre+Baskerville:wght@700&family=Sorts+Mill+Goudy&display=swap">
<style>
  :root {
    --dirt-light: #9c7d5e;
    --dirt-mid: #7a5c41;
    --dirt-dark: #4e3826;
    --charcoal: #352f2f;
    --ink: #151111;
    --orange: #ec7a1e;
    --machine-dark: #1b1717;
  }
  * { margin: 0; padding: 0; box-sizing: border-box; }
  html, body { width: 1200px; height: 693px; overflow: hidden; }
  .card {
    position: relative;
    width: 1200px;
    height: 693px;
    background: radial-gradient(ellipse at 40% 45%, var(--dirt-light), var(--dirt-mid) 55%, var(--dirt-dark));
  }
  .panel {
    position: absolute;
    left: 45px;
    top: 47px;
    width: 1107px;
    height: 602px;
    background: var(--charcoal);
  }
  .brand-name {
    position: absolute;
    left: 0;
    width: 100%;
    text-align: center;
    font-family: "Alfa Slab One", serif;
    color: var(--ink);
    -webkit-text-stroke: 2px var(--orange);
    line-height: 1;
  }
  .brand-name .line-one {
    display: block;
    font-size: 84px;
    margin-top: 10px;
  }
  .brand-name .line-two {
    display: block;
    font-size: 82px;
    letter-spacing: -1px;
    margin-top: -4px;
  }
  .tagline {
    position: absolute;
    top: 207px;
    left: 0;
    width: 100%;
    text-align: center;
    padding-right: 130px;
    font-family: "Sorts Mill Goudy", serif;
    font-size: 46px;
    color: var(--ink);
    -webkit-text-stroke: 1.2px var(--orange);
  }
  .machine-art {
    position: absolute;
    left: 6px;
    top: 331px;
    width: 514px;
    height: 271px;
    background: linear-gradient(135deg, var(--machine-dark) 0%, #2a211c 70%, #5a3717 100%);
  }
  .contact {
    position: absolute;
    right: 6px;
    top: 322px;
    text-align: right;
    color: var(--ink);
  }
  .contact .person {
    font-family: "Alfa Slab One", serif;
    font-size: 54px;
    line-height: 64px;
    -webkit-text-stroke: 1.5px var(--orange);
  }
  .contact .detail {
    font-family: "Libre Baskerville", serif;
    font-weight: 700;
    font-size: 37px;
    line-height: 54px;
    -webkit-text-stroke: 1px var(--orange);
  }
  .contact .detail.email {
    font-size: 27px;
  }
</style>
</head>
<body>
  <div class="card">
    <div class="panel">
      <h1 class="brand-name">
        <span class="line-one">Tall Creek</span>
        <span class="line-two">Groundworks Solutions</span>
      </h1>
      <p class="tagline">Backhoe and Truck Hire</p>
      <div class="machine-art" role="img" aria-label="Silhouette illustration of a backhoe excavator outlined in orange, tipping soil from its bucket"></div>
      <div class="contact">
        <p class="person">Peter Kellow</p>
        <p class="detail">Phone: 0491 736 204</p>
        <p class="detail">Phone: 0491 862 035</p>
        <p class="detail email">tcgsolutions@mailbox-example.com</p>
        <p class="detail">ABN:58214096371</p>
      </div>
    </div>
  </div>
</body>
</html>
```